Redesign website for small print company

Vindaborgprent is a small printing company in Iceland mainly servicing Students, schools, etc. We are also doing all kind of other jobs, like business cards, book printing, brochure printing etc. We are also selling books online.
Our website is: www.vindaborgprent.is
What we are looking for is:
- Web Design (Uncoded - PSD layout only)
- Mobile friendly design, using our current color scheme: Red, green, yellow and light gray.
- Clean simple design
- Simple, light and easy to use.
- More menu Items/drop down
Industry/Entity Type
Digital Printing
Number of Pages Required
5+ page
Requirements
Must have
- Easy navigation
- Designed for mobile
- Current color scheme (see logo)
Nice to have
- Icon based products

```html
<!DOCTYPE html>
<html lang="is">
<head>
<meta charset="utf-8">
<title>Vindaborgprent</title>
<link href="https://fonts.googleapis.com/css2?family=Poppins:wght@300;400;500;600;700&display=swap" rel="stylesheet">
<style>
:root{
  --red:#e8312f;
  --yellow:#fbd200;
  --green:#146b35;
  --ink:#1d1d1d;
  --text:#6f6f6f;
  --muted:#9a9a9a;
  --light:#f4f4f4;
  --line:#e6e6e6;
  --map-a:#cfe0ee;
  --map-b:#e3e6e9;
  --footer:#3d3d3d;
}
*{margin:0;padding:0;box-sizing:border-box}
html,body{width:1200px;height:2853px;overflow:hidden;background:#fff}
body{font-family:"Poppins",sans-serif;color:var(--ink);position:relative}
.abs{position:absolute}

.topbar{left:0;top:0;width:1200px;height:53px;border-bottom:1px solid var(--line);font-size:13px;display:flex;align-items:center;padding-left:91px;gap:14px}
.topbar .phone{color:var(--red);font-weight:600;font-size:15px}
.topbar .email{color:var(--green)}
.topbar .lang{position:absolute;left:1020px;color:var(--muted);display:flex;align-items:center;gap:8px}
.topbar .flag{width:22px;height:13px;background:#2b3c8f;display:inline-block}

.nav{left:0;top:53px;width:1200px;height:71px;box-shadow:0 2px 6px rgba(0,0,0,.05)}
.brand{display:flex;align-items:center;gap:8px;font-weight:700;font-size:22px;color:var(--ink)}
.brand .mark{width:26px;height:26px;background:var(--red)}
.nav .brand{position:absolute;left:86px;top:20px}
.menu a{position:absolute;top:28px;font-size:12.5px;font-weight:500;color:var(--ink);text-decoration:none}

.hero{left:0;top:124px;width:1200px;height:447px;background:linear-gradient(#ffffff,#f3f3f3)}
.hero-photo{left:219px;top:45px;width:770px;height:402px;background:linear-gradient(90deg,#cfd7e3,#e9c8c8 45%,#c9d6e8 70%,#eadbd0);border-radius:4px}

.action{width:152px;height:152px;border-radius:50%;display:flex;flex-direction:column;align-items:center;justify-content:center;font-weight:700;font-size:15px;gap:10px;box-shadow:0 6px 14px rgba(0,0,0,.12)}
.action.yellow{background:var(--yellow);color:var(--ink)}
.action.red{background:var(--red);color:#fff}
.action.green{background:var(--green);color:#fff}

.wave{left:0;top:1120px;width:1200px;height:560px}

.eyebrow{font-size:14px;letter-spacing:1px;color:var(--muted);font-weight:500}
.section-title{font-size:38px;font-weight:600;color:var(--ink)}

.card{width:316px;height:291px;background:#fff;box-shadow:0 4px 18px rgba(0,0,0,.06);display:flex;flex-direction:column;align-items:center}
.card .icon{width:60px;height:60px;margin-top:72px;border-radius:6px}
.card h3{font-size:21px;font-weight:500;margin-top:22px}
.card .arrow{margin-top:26px}

.about-mark{left:185px;top:1788px;width:214px;height:276px;display:flex;flex-direction:column;align-items:center;justify-content:center;gap:18px}
.about-mark .square{width:150px;height:150px;background:var(--red)}
.about-mark span{font-size:22px;font-weight:700;color:var(--ink)}
.about h2{font-size:38px;font-weight:500;margin-top:18px}
.about p{font-size:13.5px;line-height:27px;color:var(--text);width:537px;font-weight:300;margin-top:24px}
.btn{display:inline-block;width:156px;height:46px;border:1px solid var(--line);box-shadow:0 2px 6px rgba(0,0,0,.06);text-align:center;line-height:46px;font-size:14px;font-weight:500}

.map{left:0;top:2235px;width:1200px;height:489px;background:linear-gradient(120deg,var(--map-a),var(--map-b) 60%)}
.contact{left:97px;top:2324px;width:302px;height:301px;background:#fff;box-shadow:0 6px 20px rgba(0,0,0,.15);padding:32px 40px}
.contact .brand{font-size:21px}
.contact ul{list-style:none;margin-top:22px;font-size:12.5px;line-height:22px;color:#444}
.social{display:flex;gap:10px;margin-top:16px}
.social i{width:28px;height:28px;border-radius:50%;display:block}

.footer{left:0;top:2724px;width:1200px;height:129px;background:var(--footer);color:#fff;font-size:12.5px}
.footer .links{position:absolute;left:95px;top:40px;display:flex;gap:26px}
.footer .copy{position:absolute;left:95px;top:65px}
.footer .cards{position:absolute;left:1005px;top:34px;display:flex;gap:18px}
.footer .cards i{width:50px;height:32px;border:2px solid #aaa;border-radius:4px;display:block}
</style>
</head>
<body>

<div class="abs topbar">
  <span>Call: <span class="phone">555 0142</span></span><span>|</span>
  <span class="email">verk@vindaborgprent.is</span><span>|</span>
  <span>Mon - Fri: 9-17</span>
  <span class="lang"><i class="flag"></i>English ⌄</span>
</div>

<header class="abs nav">
  <div class="brand"><i class="mark"></i>VINDABORGPRENT</div>
  <nav class="menu">
    <a style="left:443px">HOME</a>
    <a style="left:525px">SERVICES</a>
    <a style="left:633px">BOOKS</a>
    <a style="left:707px">JOB SUBMIT</a>
    <a style="left:822px">ABOUT US</a>
    <a style="left:917px">CONTACT US</a>
  </nav>
  <svg class="abs" style="left:1038px;top:21px" width="26" height="26" viewBox="0 0 26 26" fill="none" stroke="#1d1d1d" stroke-width="2.4"><circle cx="11" cy="11" r="8"/><path d="M17 17l7 7"/></svg>
  <svg class="abs" style="left:1083px;top:18px" width="34" height="32" viewBox="0 0 34 32" fill="none" stroke="#1d1d1d" stroke-width="2.2"><path d="M2 5h5l4 16h15l4-11H9"/><circle cx="13" cy="27" r="2"/><circle cx="24" cy="27" r="2"/><circle cx="29" cy="5" r="4" fill="#fbd200" stroke="none"/></svg>
</header>

<section class="abs hero">
  <div class="abs hero-photo" role="img" aria-label="Group of smiling students holding notebooks and folders"></div>
</section>

<div class="abs action yellow" style="left:291px;top:538px">
  <svg width="40" height="34" viewBox="0 0 40 34" fill="none" stroke="#1d1d1d" stroke-width="2.4"><rect x="3" y="9" width="34" height="22" rx="3"/><path d="M14 9V4h12v5M3 18h34"/></svg>
  SENDA VERK
</div>
<div class="abs action red" style="left:525px;top:538px">
  <svg width="40" height="40" viewBox="0 0 40 40" fill="none" stroke="#fff" stroke-width="2.4"><circle cx="20" cy="20" r="16"/><circle cx="13" cy="15" r="2.5"/><circle cx="21" cy="11" r="2.5"/><circle cx="28" cy="17" r="2.5"/></svg>
  HANNA VERK
</div>
<div class="abs action green" style="left:774px;top:538px">
  <svg width="36" height="44" viewBox="0 0 36 44" fill="none" stroke="#fff" stroke-width="2.4"><path d="M18 3c8 7 9 18 6 28H12C9 21 10 10 18 3z"/><path d="M13 24l4 4 7-8"/><path d="M12 31l-6 7M24 31l6 7"/></svg>
  FA TILBOD
</div>

<svg class="abs wave" viewBox="0 0 1200 560" preserveAspectRatio="none"><path d="M0 0 C300 40 900 40 1200 0 L1200 250 C900 330 600 380 430 470 C330 520 200 560 0 500 Z" fill="#f3f3f3"/></svg>

<div class="abs eyebrow" style="left:0;width:1200px;text-align:center;top:752px">SERVICES</div>
<h2 class="abs section-title" style="left:0;width:1200px;text-align:center;top:778px">We Offer Below Services</h2>

<div class="abs card" style="left:86px;top:890px"><div class="icon" role="img" aria-label="Pencil and paper icon" style="background:linear-gradient(#fbd200,#e8a100)"></div><h3>Essays</h3><svg class="arrow" width="24" height="10"><path d="M0 5h22M17 1l5 4-5 4" stroke="#c4c4c4" stroke-width="2" fill="none"/></svg></div>
<div class="abs card" style="left:441px;top:890px"><div class="icon" role="img" aria-label="Business card holder icon" style="background:linear-gradient(#f0a0a0,#e8312f)"></div><h3>Business Cards</h3><svg class="arrow" width="24" height="10"><path d="M0 5h22M17 1l5 4-5 4" stroke="#c4c4c4" stroke-width="2" fill="none"/></svg></div>
<div class="abs card" style="left:799px;top:890px"><div class="icon" role="img" aria-label="Folded leaflet icon" style="background:linear-gradient(#e7f1d9,#7fb26f)"></div><h3>Leafleats</h3><svg class="arrow" width="24" height="10"><path d="M0 5h22M17 1l5 4-5 4" stroke="#c4c4c4" stroke-width="2" fill="none"/></svg></div>
<div class="abs card" style="left:86px;top:1236px"><div class="icon" role="img" aria-label="Books on a shelf icon" style="background:linear-gradient(90deg,#e8312f,#fbd200,#35a15a,#3a7bd5)"></div><h3>Book Printing</h3><svg class="arrow" width="24" height="10"><path d="M0 5h22M17 1l5 4-5 4" stroke="#c4c4c4" stroke-width="2" fill="none"/></svg></div>
<div class="abs card" style="left:441px;top:1236px"><div class="icon" role="img" aria-label="Poster icon" style="background:linear-gradient(#fbd200,#f6e6a0)"></div><h3>Posters</h3><svg class="arrow" width="24" height="10"><path d="M0 5h22M17 1l5 4-5 4" stroke="#c4c4c4" stroke-width="2" fill="none"/></svg></div>
<div class="abs card" style="left:799px;top:1236px"><div class="icon" role="img" aria-label="Red textbook icon" style="background:linear-gradient(#f26a5e,#d8322c)"></div><h3>Textbooks</h3><svg class="arrow" width="24" height="10"><path d="M0 5h22M17 1l5 4-5 4" stroke="#c4c4c4" stroke-width="2" fill="none"/></svg></div>

<div class="abs about-mark"><i class="square"></i><span>Vindaborgprent</span></div>

<section class="abs about" style="left:518px;top:1674px">
  <div class="eyebrow">ABOUT US</div>
  <h2>Velkomin í Vindaborgprent</h2>
  <p>Vindaborgprent er fyrirtæki staðsett á háskólasvæðinu sem hefur sérhæft sig í að þjónusta skólafólk, ásamt því að sinna allri almennri prentun fyrir almenning.</p>
  <p>Vindaborgprent gefur út greinasöfn og frumsamdar kennslubækur fyrir námskeið, prentar lokaritgerðir fyrir nema, auk þess að vinna við ótalinn fjölda smærri verka fyrir nemendur, kennara og stofnanir. Má þar nefna bæklinga, skýrslur, spurningalista, nafnspjöld, bækur, OCR skönnun og fleira.</p>
  <p>Vindaborgprent er umhverfisvottuð prentsmiðja. Laufmerkið er opinbert umhverfismerki Norðurlandanna, sem hefur skapað sér fótfestu hér á landi og er þekkt meðal neytenda.</p>
  <div class="btn" style="margin-top:30px">More About Us</div>
</section>

<div class="abs map" role="img" aria-label="Map showing the shop location in central Reykjavík"></div>

<div class="abs contact">
  <div class="brand"><i class="mark"></i>VINDABORGPRENT</div>
  <ul>
    <li>Vindaborgprent. Kt: 410293-2270</li>
    <li>Hrafnagata 7</li>
    <li>107 Reykjavík</li>
    <li>Vsk: 204518</li>
    <li>IBAN IS00 0000 1234 5678 9012 3456</li>
    <li>78</li>
    <li>SWIFT (BIC) VNDBISRE</li>
  </ul>
  <div class="social"><i style="background:var(--yellow)"></i><i style="background:#222"></i><i style="background:#2d6fb7"></i><i style="background:var(--red)"></i></div>
</div>

<footer class="abs footer">
  <div class="links"><span>Home</span><span>Services</span><span>Skil á verkum</span><span>To okkur</span></div>
  <div class="copy">© 2018, Vindaborgprent</div>
  <div class="cards"><i></i><i></i></div>
</footer>

</body>
</html>
```